Water Filtration Company needs a business card design using our existing logo/colours!

We design and manufacture and export specialised water filtration equipment. Our equipment will take unclean dirty water and filters to safe clean drinkable water.
We would like to see designs using our existing logo and colours (see attached "Palette") that represents clean safe drinking water (fresh, clean designs but still professional and modern). Our customers are other businesses who supply water filtration equipment, governments, and private individuals.
BUSINESS CARD DETAILS (Common details):
Tel: + 61 7 55 914 372
www: brenvalegroup.com.au
Address: 3/41 Corbett Lane
Kellow Ridge NSW 2517 Australia
(please include the word Australia as we are an international company)
Must include: COMMERCIAL WATER FILTRATION EQUIPMENT
NAME NO 1:
Dennis Harper
General Manager
Mobile: +61 418 27 93 40
Email: dennis@brenvalegroup.com.au
NAME NO. 2:
Karen Poe
Business Manager
Mobile: +61 416 572 814
Email: karen@brenvalegroup.com.au
Must Have:
1) PRINT READY IN .AI & .PDF FORMATS
2) Also saved in file format .ai (Adobe Illustrator - compatible with CS4)
3) Use existing LOGO & COLOURS: Please use our logo (see attached file)
4) FONTS: we have used Avenir & Helvetica in the past but are open to other font types for the address etc.
Thank you!

```html
<!DOCTYPE html>
<html lang="en">
<head>
<meta charset="utf-8">
<title>Brenvale business card – front and back</title>
<link rel="stylesheet" href="https://fonts.googleapis.com/css2?family=Electrolize&display=swap">
<style>
  :root {
    --page: #fffaf3;
    --card-blue: #b8e2ea;
    --card-white: #ffffff;
    --ink: #1b6485;
    --shadow: rgba(60, 80, 90, 0.18);
  }
  * { margin: 0; padding: 0; box-sizing: border-box; }
  html, body {
    width: 1200px;
    height: 1000px;
    overflow: hidden;
    background: var(--page);
  }
  body {
    position: relative;
    font-family: "Electrolize", "Trebuchet MS", sans-serif;
    color: var(--ink);
  }
  .card {
    position: absolute;
    top: 347px;
    width: 543px;
    height: 306px;
    border-radius: 14px;
    overflow: hidden;
    background: var(--card-blue);
    box-shadow: 0 6px 14px var(--shadow);
  }
  .card--front { left: 27px; }
  .card--back { left: 626px; }
  .card__wedge {
    position: absolute;
    inset: 0;
    width: 543px;
    height: 306px;
  }
  .brand {
    position: absolute;
    left: 30px;
    top: 40px;
    display: flex;
    align-items: center;
    gap: 10px;
    font-size: 46px;
    line-height: 1;
    letter-spacing: 1px;
    color: var(--ink);
  }
  .brand__dot {
    width: 16px;
    height: 16px;
    border-radius: 50%;
    background: var(--ink);
  }
  .tagline {
    position: absolute;
    left: 31px;
    top: 96px;
    font-size: 10px;
    line-height: 12px;
    letter-spacing: 1.2px;
    color: var(--ink);
    white-space: nowrap;
  }
  .person {
    position: absolute;
    left: 30px;
    top: 160px;
  }
  .person__name {
    font-size: 24px;
    line-height: 26px;
    letter-spacing: 1px;
  }
  .person__role {
    font-size: 16px;
    line-height: 18px;
    letter-spacing: 1px;
  }
  .person__contact {
    margin-top: 16px;
    font-size: 16px;
    line-height: 18px;
    letter-spacing: 1.2px;
  }
  .company-details {
    position: absolute;
    left: 30px;
    top: 164px;
    font-size: 16px;
    line-height: 23px;
    letter-spacing: 1.2px;
  }
</style>
</head>
<body>
  <article class="card card--front">
    <svg class="card__wedge" viewBox="0 0 543 306" aria-hidden="true">
      <polygon points="518,0 543,0 543,306 335,306" fill="var(--card-white)"/>
    </svg>
    <div class="brand"><span class="brand__name">brenvale</span><span class="brand__dot"></span></div>
    <p class="tagline">COMMERCIAL WATER FILTRATION EQUIPMENT</p>
    <div class="person">
      <p class="person__name">Dennis Harper</p>
      <p class="person__role">General Manager</p>
      <p class="person__contact">Mobile: +61 418 27 93 40<br>Email: dennis@brenvalegroup.com.au</p>
    </div>
  </article>

  <article class="card card--back">
    <svg class="card__wedge" viewBox="0 0 543 306" aria-hidden="true">
      <polygon points="518,0 543,0 543,306 335,306" fill="var(--card-white)"/>
    </svg>
    <div class="brand"><span class="brand__name">brenvale</span><span class="brand__dot"></span></div>
    <p class="tagline">COMMERCIAL WATER FILTRATION EQUIPMENT</p>
    <div class="company-details">
      <p>Tel: + 61 7 55 914 372</p>
      <p>www: brenvalegroup.com.au</p>
      <p>Address: 3/41 Corbett Lane</p>
      <p>Kellow Ridge NSW 2517</p>
      <p>Australia</p>
    </div>
  </article>
</body>
</html>
```